Flyer promoting Velmora's workshops and credentials

We run Training workshops for the data analyst community. We'd like a flyer to sell our services using a style and colour scheme consistent with our website www.velmoraskills.co.uk . I've attached some background info and some existing e-brochures for different workshops to give a flavour for content (but these are poorly designed and we don't want a similar design!!). There's also an overview document which gives more direction. The flyer will be sent with an accompanying letter to Learning & Development decision makers as well as Anlaytical team managers. It's purpose would be to generate enquiries and bookings for primarliy our flagship workshop 'Turning Figures Into Real Results'.

Target Market(s)

Learning and Development senior managers
Analytical team managers

Industry/Entity Type

Training

Font styles to use
Other font styles liked:
• Similar to website for consistency

Requirements
Must have
• Good copy! Slick design more in line with European (UK) style advertising rather than US.
Nice to have
• Some humour,
Should not have
• should not be as boring and non-sales based as the website!! Website is not a great example!

```html
<!DOCTYPE html>
<html lang="en">
<head>
<meta charset="utf-8">
<title>Velmora – Workshops for Data Analysts</title>
<link rel="stylesheet" href="https://fonts.googleapis.com/css2?family=Fira+Sans:ital,wght@0,400;0,500;0,600;0,700;1,400&display=swap">
<style>
  :root {
    --navy: #2a4a7f;
    --navy-deep: #1f3a68;
    --orange: #e07b25;
    --paper: #f4f5f7;
    --header-grey: #e9eaed;
    --ink: #23395f;
    --backdrop: #d9dadc;
  }
  * { box-sizing: border-box; margin: 0; padding: 0; }
  html, body { width: 1200px; height: 960px; overflow: hidden; }
  body {
    background: var(--backdrop);
    font-family: "Fira Sans", sans-serif;
    color: var(--ink);
    position: relative;
  }
  .page {
    position: absolute; top: 0;
    width: 585px; height: 960px;
    background: var(--paper);
    overflow: hidden;
  }
  .page-front { left: 8px; }
  .page-back { left: 607px; }

  /* ---------- front page ---------- */
  .header-shapes { position: absolute; left: 0; top: 0; }
  .brand { position: absolute; left: 60px; top: 24px; }
  .brand-name {
    font-size: 44px; font-weight: 600; color: var(--navy);
    line-height: 1; letter-spacing: -0.5px;
  }
  .brand-tag {
    font-size: 13px; font-weight: 500; color: var(--orange);
    margin-left: 48px; margin-top: 2px;
  }
  .hero-photo {
    position: absolute; left: 0; top: 125px;
    width: 585px; height: 285px;
    background:
      radial-gradient(circle at 28% 45%, rgba(224,123,37,0.35), transparent 35%),
      linear-gradient(100deg, #8d8f93 0%, #a7a8ab 40%, #5b5553 70%, #8a8b8e 100%);
  }
  .headline-band { position: absolute; left: 0; top: 350px; }
  .headline {
    position: absolute; left: 200px; top: 364px; width: 370px;
    color: #fff; font-size: 19px; font-weight: 400; line-height: 28px; letter-spacing: 0.3px;
    text-align: right;
  }
  .intro {
    position: absolute; left: 30px; top: 482px; width: 530px;
    font-size: 11.8px; line-height: 17px;
  }
  .intro p + p { margin-top: 9px; }
  .intro strong { font-weight: 700; }
  .section-title {
    position: absolute; left: 22px; top: 770px;
    font-size: 23px; font-weight: 600; letter-spacing: 1px; color: var(--navy-deep);
    background: var(--paper); padding: 0 8px; line-height: 30px;
  }
  .section-rule {
    position: absolute; left: 0; top: 784px; width: 585px; height: 3px;
    background: var(--navy-deep);
  }
  .section-rule.thin { top: 806px; left: 200px; width: 385px; height: 1px; }
  .quote {
    position: absolute; top: 820px; height: 88px;
    color: #fff; font-size: 11px; line-height: 16px; letter-spacing: 0.3px;
    padding: 10px 14px;
  }
  .quote-blue { left: 0; width: 325px; background: var(--navy); }
  .quote-orange { left: 325px; width: 260px; background: var(--orange); }
  .footer-rule {
    position: absolute; left: 18px; top: 914px; width: 549px; height: 2px;
    background: var(--navy-deep);
  }
  .footer {
    position: absolute; left: 0; bottom: 0; width: 585px; height: 36px;
    background: var(--navy-deep);
    border-top: 3px solid var(--orange);
    color: #fff; font-size: 12.5px; font-weight: 500; letter-spacing: 0.3px;
    display: flex; align-items: center; justify-content: center;
  }

  /* ---------- back page ---------- */
  .back-top { position: absolute; left: 0; top: 0; width: 585px; height: 96px; display: flex; }
  .back-intro {
    width: 335px; background: var(--navy); color: #fff;
    font-size: 10.5px; line-height: 17px; padding: 12px 16px;
  }
  .discount {
    flex: 1; background: var(--orange); color: #fff;
    font-size: 8.5px; line-height: 14px; padding: 12px 12px;
  }
  .discount strong { font-size: 10.5px; font-weight: 600; }
  .directory-title {
    position: absolute; left: 22px; top: 110px;
    font-size: 22px; font-weight: 600; color: var(--navy); letter-spacing: 0.5px;
    border-bottom: 2px solid var(--navy); padding-bottom: 3px;
  }
  .directory {
    position: absolute; left: 20px; top: 152px; width: 545px;
  }
  .dir-row {
    display: grid; grid-template-columns: 132px 44px 228px 1fr;
    border: 2px solid var(--navy); margin-bottom: 7px;
    min-height: 88px; background: #fff;
  }
  .dir-row.alt { border-color: var(--orange); }
  .dir-row > div { padding: 8px 8px; border-left: 1px solid #b9c3d6; font-size: 9.5px; line-height: 14px; }
  .dir-row > div:first-child { border-left: none; }
  .dir-head {
    min-height: 0; border: none; border-bottom: 2px solid var(--navy); background: transparent;
    margin-bottom: 5px;
  }
  .dir-head > div { font-size: 11px; font-weight: 600; letter-spacing: 0.5px; padding: 3px 8px; }
  .dir-name { font-weight: 600; text-transform: uppercase; font-size: 9.5px; letter-spacing: 0.3px; display: flex; align-items: center; }
  .dir-days { font-size: 13px !important; display: flex; align-items: center; justify-content: center; }
  .dir-desc { display: flex; align-items: center; }
  .dir-audience { font-size: 8.5px !important; line-height: 13px !important; display: flex; align-items: center; }
  .back-rule {
    position: absolute; left: 20px; width: 545px; height: 2px; background: var(--navy);
  }
  .back-rule.top { top: 668px; }
  .back-rule.bottom { top: 906px; }
  .back-quotes { position: absolute; left: 24px; top: 682px; width: 540px; }
  .back-quote { font-size: 9.8px; line-height: 15px; margin-bottom: 12px; }
  .back-quote.orange { color: var(--orange); }
  .back-quote cite { display: block; font-style: normal; font-size: 9px; font-weight: 500; }
</style>
</head>
<body>
  <main class="page page-front">
    <svg class="header-shapes" width="585" height="130" viewBox="0 0 585 130" aria-hidden="true">
      <rect width="585" height="130" fill="var(--header-grey)"/>
      <polygon points="262,0 585,0 585,125 310,125" fill="var(--navy)"/>
      <polygon points="252,0 262,0 312,125 302,125" fill="var(--orange)"/>
      <rect x="0" y="120" width="305" height="5" fill="var(--navy)"/>
    </svg>

    <div class="brand">
      <div class="brand-name">Velmora</div>
      <div class="brand-tag">Workshops for Data Analysts</div>
    </div>

    <div class="hero-photo" role="img" aria-label="Photo of an analyst leaning over a laptop surrounded by sketched orange charts and graphs"></div>

    <svg class="headline-band" width="585" height="130" viewBox="0 0 585 130" aria-hidden="true">
      <polygon points="185,0 520,0 585,115 205,125" fill="var(--navy)" opacity="0.94"/>
      <polygon points="548,55 585,55 585,115" fill="var(--orange)"/>
      <rect x="0" y="108" width="200" height="2" fill="var(--navy)"/>
    </svg>
    <h1 class="headline">Do you want your data analysts to have a greater impact on your organisation AND be more productive?</h1>

    <section class="intro">
      <p>Velmora understand that technical ability alone is not enough to be effective as a data analyst. Whether you're an insight expert, a risk analyst or a Business Intelligence professional, the best analysts employ a range of complimentary soft skills in order to be able to effectively plan, present and communicate ideas, results and reports. Our range of workshops aim to help analysts become more commercially focussed and employ some key techniques and behaviours in order to maximise their influence over their key decision makers.</p>
      <p>Our workshops have been attended by many of the UK's largest organisations and many international organisations too including Corvex, Brightmere Bank, Tarnwell Energy and XXX.</p>
      <p>Our workshops are run by experienced professionals including Daniel Ashcroft, Velmora's founder and the facilitator for Velmora's flagship workshop <strong>'Turning Figures Into Real Results'</strong> - a workshop that has been running for over 10 years and become an essential 'cornerstone' development session for many of our regular clients' analysts. We aim for our workshops to be educational, interactive, practical and fun – we believe we deliver on this but don't just take our word for it, here are some comments from our clients.</p>
    </section>

    <div class="section-rule"></div>
    <div class="section-rule thin"></div>
    <h2 class="section-title">TESTIMONIALS</h2>

    <blockquote class="quote quote-blue">"Really good/interesting. Makes you think about your actions/behaviours a lot more. Will be able to apply this to your everyday life." - Analyst, Harlow Insurance</blockquote>
    <blockquote class="quote quote-orange">"A very useful course with a very engaging trainer. Excellent examples that related to our work."<br>– Delegate, Northline Rail</blockquote>

    <div class="footer-rule"></div>
    <footer class="footer">www.velmoraskills.co.uk &nbsp;|&nbsp; Tel 0161 555 0142 &nbsp;|&nbsp; email: info@velmoraskills.co.uk</footer>
  </main>

  <section class="page page-back">
    <div class="back-top">
      <p class="back-intro">All of our workshops are interactive and practical. Analysts can attend one of the scheduled public workshops or if you have several analysts, an on-site private workshop offers significant savings and the chance to work through challenges as a team.</p>
      <p class="discount">Any bookings made with reference to this flyer will benefit from <strong>A 10% DISCOUNT</strong> on fees until February 18th 2016.<br>*(This may not be used in conjunction with any other promotional rate that may be available at the time of booking).*</p>
    </div>

    <h2 class="directory-title">Workshop Directory</h2>

    <div class="directory">
      <div class="dir-row dir-head">
        <div>TITLE</div><div>DAYS</div><div>DESCRIPTION</div><div>AUDIENCE</div>
      </div>
      <div class="dir-row">
        <div class="dir-name">Turning Figures Into Real Results</div>
        <div class="dir-days">2</div>
        <div class="dir-desc">A CPD accredited, interactive soft-skills workshop to improve the productivity and impact an analyst has on the organisation they support.</div>
        <div class="dir-audience">Marketing Analysts, MI / BI Analysts<br>Risk Analysts, MI Analysts<br>Statistical Analysts, Financial Analysts.</div>
      </div>
      <div class="dir-row alt">
        <div class="dir-name">Selling Analysis With Impact</div>
        <div class="dir-days">0.5</div>
        <div class="dir-desc">A half day seminar on the key behaviours and techniques information analysts/insight specialists need to employ in order to have a positive impact on their internal or external customers.</div>
        <div class="dir-audience">MI / BI Analysts<br>Risk Analysts<br>Insight/Marketing Analysts<br>Statistical Analysts<br>Team managers.</div>
      </div>
      <div class="dir-row">
        <div class="dir-name">Influencing Skills</div>
        <div class="dir-days">1</div>
        <div class="dir-desc">This workshop equips the analyst with a set of established techniques and principals to help them effectively influence their customers and internal decision makers - a key skill to ensuring personal and commercial goals are achieved.</div>
        <div class="dir-audience">Marketing Analysts<br>MI / BI Analysts<br>Risk Analysts<br>Insight Analysts<br>Statistical Analysts<br>Financial Analysts.</div>
      </div>
      <div class="dir-row alt">
        <div class="dir-name">Analytics in Direct Marketing</div>
        <div class="dir-days">1</div>
        <div class="dir-desc">A workshop to help delegates understand the tactical and strategic analytics which support the direct marketing life cycle. Includes practical exercises to reinforce the learnings. This workshop can only be hosted privately.</div>
        <div class="dir-audience">Marketing Analysts<br>Direct Marketers</div>
      </div>
      <div class="dir-row">
        <div class="dir-name">Bespoke Statistical Workshops</div>
        <div class="dir-days">1</div>
        <div class="dir-desc">Customisable workshops - select the statistical methods and techniques you and your colleagues would like to cover and we'll provide you with a tailored day with practical examples and accompanying notes.</div>
        <div class="dir-audience">Data Analysts<br>Statistical Analysts<br>Insight Analysts</div>
      </div>
    </div>

    <div class="back-rule top"></div>
    <div class="back-quotes">
      <blockquote class="back-quote">"I took from the course a number of actionable learnings that we have put into practice and this has resulted in positive feedback and a happier more valued team. Recommend the course to new and experienced analysts alike."<cite>P. Garland, Fairhaven Aid</cite></blockquote>
      <blockquote class="back-quote orange">"The workshop covered a lot of the areas I was concerned about in my role and how things were connected. It has given me the confidence to alter some of my ways of working so I work more efficiently."<cite>J. Mercer, Kestrel Ltd</cite></blockquote>
      <blockquote class="back-quote">"An excellent balance of approach, attitude and methodology with technical competency based analysis techniques. Provides a clear framework for universal practice within an analytical team."<cite>R. Whitby, Ledger Media Group</cite></blockquote>
    </div>
    <div class="back-rule bottom"></div>
    <footer class="footer">www.velmoraskills.co.uk &nbsp;|&nbsp; Tel 0161 555 0142 &nbsp;|&nbsp; email: info@velmoraskills.co.uk</footer>
  </section>
</body>
</html>
```